I would like to start a new webpage for a dating site in switzerland.
The dating site is not a escort service at all and should not transmit any type of sexual connotation.
The is more a compagnionship dating : male pay to meet ladies for some time in which they invite them for dinner, coktail, museum visit or walking or even skying. the meeting will take place in big cities in switzerland: geneva, zurich, bern, lausannes.

Industry/Entity Type

Dating

```html
<!DOCTYPE html>
<html lang="en">
<head>
<meta charset="utf-8">
<title>Alpen Rendezvous</title>
<link rel="stylesheet" href="https://fonts.googleapis.com/css2?family=Raleway:wght@400;500&family=Lato:wght@400&family=Courgette&display=swap">
<style>
:root{
  --accent:#ee4a52;
  --ink:#333333;
  --muted:#666666;
  --line:#e3e3e3;
  --panel:#f7f7f7;
  --footer:#2b2b2b;
  --white:#ffffff;
}
*{box-sizing:border-box;margin:0;padding:0}
html,body{width:874px;height:1200px;overflow:hidden;background:var(--white)}
body{position:relative;font-family:"Lato",sans-serif;color:var(--ink)}
.abs{position:absolute}

/* header */
.brand{left:95px;top:20px;font-family:"Raleway",sans-serif;font-size:28px;font-weight:400;color:var(--ink);letter-spacing:-.3px}
.nav{left:357px;top:30px;display:flex;align-items:center;font-family:"Raleway",sans-serif;font-size:10px;color:var(--ink)}
.nav a{color:inherit;text-decoration:none;padding:0 10px;border-left:1px solid var(--line);line-height:16px}
.nav a.current{border:1px solid var(--accent);color:var(--accent);padding:4px 12px;margin-right:2px}
.nav a.current + a{border-left:none}

/* hero */
.hero{left:0;top:70px;width:874px;height:370px;background:linear-gradient(180deg,#b9c7d1 0%,#8fa6b8 45%,#6f8ea7 70%,#c7cfd4 100%)}
.hero-people{left:300px;top:70px;width:480px;height:370px;background:radial-gradient(ellipse at 55% 45%,#e8d6c8 0%,#d8b8a2 35%,rgba(210,200,195,.4) 70%,rgba(0,0,0,0) 100%)}
.hero-next{left:763px;top:236px;width:37px;height:37px;border-radius:50%;background:#555b61}
.join{left:95px;top:127px;width:211px;height:260px;background:var(--white);box-shadow:0 0 4px rgba(0,0,0,.15);padding:0 26px}
.join h2{font-family:"Courgette",cursive;font-weight:400;font-size:25px;color:var(--ink);margin-top:15px;text-align:right;letter-spacing:-.3px}
.join h2 span{color:var(--accent)}
.join .sub{font-family:"Raleway",sans-serif;font-size:10px;color:#888;text-align:right;margin-top:3px;padding-bottom:8px;border-bottom:1px solid var(--line)}
.join label{display:block;font-size:8px;color:#555;margin-top:9px}
.field{height:21px;border:1px solid var(--line);font-size:8px;color:#555;padding:0 7px;display:flex;align-items:center;justify-content:space-between}
.row{display:flex;align-items:center;gap:11px;margin-top:4px}
.row .field{width:55px}
.row span{font-size:8.5px;color:#555}
.mt{margin-top:9px}
.caret{width:0;height:0;border-left:2.5px solid transparent;border-right:2.5px solid transparent;border-top:3px solid #444}
.search{display:block;margin:13px auto 0;width:71px;height:25px;background:var(--accent);color:var(--white);font-family:"Courgette",cursive;font-size:13px;text-align:center;line-height:25px}

/* feature cards */
.card{top:500px;width:211px;height:250px;background:var(--panel);text-align:center}
.card .photo{height:125px}
.card h3{font-family:"Raleway",sans-serif;font-weight:400;font-size:17px;color:var(--accent);margin-top:15px}
.card p{font-size:9.5px;line-height:15px;color:var(--muted);margin:12px 10px 0}
.btn{display:inline-block;margin-top:12px;border:1px solid var(--accent);color:var(--accent);font-family:"Raleway",sans-serif;font-size:10px;padding:6px 13px}

/* lower sections */
.section-title{font-family:"Raleway",sans-serif;font-weight:400;font-size:19px;line-height:24px;color:var(--ink)}
.section-title span{color:var(--accent)}
.services{left:95px;top:797px;width:138px}
.services ul{list-style:none;margin-top:16px}
.services li{display:flex;align-items:center;gap:14px;font-size:9.5px;color:#444;height:30px;border-bottom:1px solid #eee}
.services li:last-child{border-bottom:none}
.bullet{width:11px;height:11px;background:#9a9a9a;flex:none;display:flex;align-items:center;justify-content:center}
.bullet.active{background:var(--accent)}
.about{left:261px;top:797px;width:334px}
.about .lead{font-size:11.5px;line-height:19px;color:#444;margin-top:14px}
.team{display:flex;gap:14px;margin-top:10px}
.member{width:160px;text-align:center}
.member .photo{height:103px}
.member h4{font-family:"Raleway",sans-serif;font-weight:400;font-size:10px;color:var(--accent);margin-top:14px}
.about .body{font-size:9px;line-height:17.5px;color:var(--muted);margin-top:17px}
.more{color:var(--accent);font-style:italic}

.news{left:621px;top:797px;width:158px}
.news-list{margin-top:25px}
.news-item{padding:0 0 3px;border-bottom:1px solid #eee}
.news-item + .news-item{padding-top:16px}
.news-item:last-child{border-bottom:none}
.date{display:inline-block;border:1px solid var(--line);color:var(--accent);font-size:9px;line-height:13px;padding:2px 5px}
.news-item p{font-size:9px;line-height:17px;color:var(--muted);margin-top:4px;padding-left:2px}
.news-item .more{display:block;font-size:9px;line-height:14px;padding-left:2px}

/* footer */
.footer{left:0;top:1125px;width:874px;height:75px;background:var(--footer)}
.footer-nav{left:96px;top:1146px;font-family:"Raleway",sans-serif;font-size:9.5px;color:#bbb}
.footer-nav span{margin:0 6px;color:#999}
.copyright{left:96px;top:1170px;font-size:9px;color:#aaa}
.social{left:681px;top:1153px;display:flex;gap:4px}
.social i{width:21px;height:21px;border-radius:50%;background:#f1f1f1;display:block}
</style>
</head>
<body>

<header>
  <div class="abs brand">Alpen Rendezvous</div>
  <nav class="abs nav">
    <a class="current">HOME</a>
    <a>ABOUT US</a>
    <a>DATING</a>
    <a>ADD PROFILE</a>
    <a>COMMUNITY</a>
    <a>CONTACT US</a>
  </nav>
</header>

<section>
  <div class="abs hero" role="img" aria-label="Beach backdrop with soft blue sea and sky"></div>
  <div class="abs hero-people" role="img" aria-label="Photo of a smiling couple embracing by the sea"></div>
  <div class="abs hero-next">
    <svg width="37" height="37" viewBox="0 0 37 37"><path d="M16 12l6 6.5-6 6.5" fill="none" stroke="#fff" stroke-width="1.5"/></svg>
  </div>

  <form class="abs join">
    <h2><span>Join,</span> it's Free!</h2>
    <div class="sub">AND START DATING TODAY!</div>
    <label>I'm a:</label>
    <div class="row">
      <div class="field">Woman <i class="caret"></i></div>
      <span>Seeking</span>
      <div class="field">Man <i class="caret"></i></div>
    </div>
    <div class="field mt">Zip Code:</div>
    <label>Country:</label>
    <div class="field" style="margin-top:4px">Switzerland <i class="caret"></i></div>
    <div class="field mt">E-mail:</div>
    <span class="search">Search</span>
  </form>
</section>

<section>
  <article class="abs card" style="left:95px">
    <div class="photo" role="img" aria-label="Portrait photo of a smiling woman" style="background:linear-gradient(135deg,#c9a78b,#8a5c45)"></div>
    <h3>Women's Gallery</h3>
    <p>Loremip ipsum dolor sit amet, consec tetuer ng elit. Praesent vestibulum molestie.</p>
    <span class="btn">MORE</span>
  </article>
  <article class="abs card" style="left:333px">
    <div class="photo" role="img" aria-label="Portrait photo of a smiling man" style="background:linear-gradient(135deg,#d9d6d2,#9a7c68)"></div>
    <h3>Men's Gallery</h3>
    <p>Loremip ipsum dolor sit amet, consec tetuer ng elit. Praesent vestibulum molestie.</p>
    <span class="btn">MORE</span>
  </article>
  <article class="abs card" style="left:568px">
    <div class="photo" role="img" aria-label="Photo of a happy couple together" style="background:linear-gradient(135deg,#eeeeee,#c8b4a6)"></div>
    <h3>Success Story</h3>
    <p>Loremip ipsum dolor sit amet, consec tetuer ng elit. Praesent vestibulum molestie.</p>
    <span class="btn">MORE</span>
  </article>
</section>

<section class="abs services">
  <h2 class="section-title">Our <span>Services</span></h2>
  <ul>
    <li><i class="bullet active"><svg width="5" height="6"><path d="M1 .5l3 2.5-3 2.5" fill="none" stroke="#fff"/></svg></i>Malesuada odiopolopol</li>
    <li><i class="bullet"><svg width="5" height="6"><path d="M1 .5l3 2.5-3 2.5" fill="none" stroke="#fff"/></svg></i>Morbnc odiof, gravida ats</li>
    <li><i class="bullet"><svg width="5" height="6"><path d="M1 .5l3 2.5-3 2.5" fill="none" stroke="#fff"/></svg></i>Cursus na loruodem</li>
    <li><i class="bullet"><svg width="5" height="6"><path d="M1 .5l3 2.5-3 2.5" fill="none" stroke="#fff"/></svg></i>Malesuada odiopolopol</li>
    <li><i class="bullet"><svg width="5" height="6"><path d="M1 .5l3 2.5-3 2.5" fill="none" stroke="#fff"/></svg></i>Morbnc odiof, gravida</li>
    <li><i class="bullet"><svg width="5" height="6"><path d="M1 .5l3 2.5-3 2.5" fill="none" stroke="#fff"/></svg></i>Malesuada odiopolopol</li>
    <li><i class="bullet"><svg width="5" height="6"><path d="M1 .5l3 2.5-3 2.5" fill="none" stroke="#fff"/></svg></i>Morbnc odiof, gravida ats</li>
    <li><i class="bullet"><svg width="5" height="6"><path d="M1 .5l3 2.5-3 2.5" fill="none" stroke="#fff"/></svg></i>Cursus na loruodem</li>
  </ul>
</section>

<section class="abs about">
  <h2 class="section-title">ABOUT US</h2>
  <p class="lead">AlpenDating is the online dating site for singles that want to get out there and meet new people!</p>
  <div class="team">
    <div class="member">
      <div class="photo" role="img" aria-label="Portrait photo of a smiling man in a light blue shirt" style="background:linear-gradient(135deg,#c7ccd0,#8fb0cf)"></div>
      <h4>MARC AEBERSOLD</h4>
    </div>
    <div class="member">
      <div class="photo" role="img" aria-label="Portrait photo of a smiling blonde woman" style="background:linear-gradient(135deg,#d8cfc6,#a8968a)"></div>
      <h4>ELENA FAVRE</h4>
    </div>
  </div>
  <p class="body">Consec tetuer adipicing it. Praesebul natoque penatibus et gnis dent mo ntes-setuidiculu. Nul laduice feugiat malesuada odiopolo. Morbnc odiof, gravida at, cursus na loruodem. &nbsp;<span class="more">Read More &gt;&gt;</span></p>
</section>

<section class="abs news">
  <h2 class="section-title">Latest <span>News</span></h2>
  <div class="news-list">
    <div class="news-item">
      <span class="date">25.09.2012</span>
      <p>Snatoque penatibus et gnis dent mo ntessetuidiculu. Nulladuice feugiat.</p>
      <span class="more">Read More &gt;&gt;</span>
    </div>
    <div class="news-item">
      <span class="date">25.09.2012</span>
      <p>Snatoque penatibus et gnis dent mo ntessetuidiculu. Nulladuice feugiat.</p>
      <span class="more">Read More &gt;&gt;</span>
    </div>
    <div class="news-item">
      <span class="date">25.09.2012</span>
      <p>Snatoque penatibus et gnis dent mo ntessetuidiculu. Nulladuice feugiat.</p>
      <span class="more">Read More &gt;&gt;</span>
    </div>
  </div>
</section>

<footer>
  <div class="abs footer"></div>
  <div class="abs footer-nav">About<span>|</span>Dating<span>|</span>Add Profile<span>|</span>Community<span>|</span>Contact</div>
  <div class="abs copyright">© 2014. alpen rendezvous. All right reserved.</div>
  <div class="abs social"><i></i><i></i><i></i><i></i></div>
</footer>

</body>
</html>
```